Amazing Sexy Elegant Eyecatching Wine Label

We need a label designed for our wine which is going to be produced very soon.

Needs to be on a grey scale, as colours increase the price per label dramatically.

Needs to have the "Crown" logo (file attached) included on the front and back label. Logo can be in black/white but can not be changed in any way, circle around the crown must stay there as well.

We are still unsure of whether to use "Harrowby Wine" or "Harrowby" as the brand for the label, if you could submit designs based around the two names we would appreciate that.

We will have 5 varieties, including; Sauvignon Blanc, Chardonnay, Pinot Gris, Riesling and Pinot Noir. So text needs to be easily changed.

We are after an image on the label which is modern and eye catching, even in a grey scale.

Please see other attached files for an idea we have done previously, we want something a bit more "designer" though. Some information on the label is a legal requirement and needs to be kept.

Target Market(s)

Wine Consumers

Requirements
Must have
• Crown Logo, Harrowby/Harrowby Wine brand, Grey Scale, Modern Design

```html
<!DOCTYPE html>
<html lang="en">
<head>
<meta charset="utf-8">
<title>Harrowby Wine – Label Range</title>
<link rel="stylesheet" href="https://fonts.googleapis.com/css2?family=Cinzel:wght@600&family=Cormorant+Garamond:wght@500&family=Open+Sans:wght@400;700&display=swap">
<style>
  :root {
    --backdrop: #e6e7e9;
    --label-black: #0d0d0e;
    --ink-white: #f2f2f2;
    --ink-grey: #b9b9bb;
    --art-dark: #2b2b2d;
    --art-mid: #55565a;
    --art-light: #c9cacd;
  }
  * { box-sizing: border-box; margin: 0; padding: 0; }
  html, body { width: 1200px; height: 1200px; overflow: hidden; }
  body {
    background: radial-gradient(circle at 50% 40%, #f7f7f8 0%, var(--backdrop) 75%);
    position: relative;
    font-family: "Open Sans", sans-serif;
    color: var(--ink-white);
  }

  /* ---------- Front label (em-scaled) ---------- */
  .front-label {
    position: absolute;
    width: 50em; height: 64em;
    background: var(--label-black);
    overflow: hidden;
    box-shadow: 0 0.6em 1.6em rgba(0,0,0,.25);
  }
  .front-label--main { left: 70px; top: 60px; font-size: 10px; }
  .front-label--variant { top: 800px; font-size: 4.9px; }

  .front-label__art {
    position: absolute; left: 0; top: 0; width: 100%; height: 42em;
    background: linear-gradient(180deg,
      var(--art-dark) 0%, #3a3b3e 48%, var(--art-mid) 50%,
      var(--art-light) 62%, #a9aaad 85%, #6b6c70 100%);
  }
  .brand-mark {
    position: absolute; left: 0; top: 3.5em; width: 100%;
    display: flex; flex-direction: column; align-items: center;
    font-family: "Cinzel", serif; font-weight: 600; color: var(--ink-white);
  }
  .brand-mark__circle {
    width: 8em; height: 8em; border-radius: 50%;
    border: 0.5em solid var(--ink-white);
    margin-bottom: 1.4em;
  }
  .brand-mark__name { font-size: 4.6em; letter-spacing: 0.06em; line-height: 1; }
  .brand-mark__sub { font-size: 2.2em; letter-spacing: 0.14em; line-height: 1.3; }

  .front-label__details {
    position: absolute; left: 0; top: 44.5em; width: 100%;
    text-align: center; color: var(--ink-white);
  }
  .front-label__region { font-size: 1.3em; letter-spacing: 0.12em; color: var(--ink-grey); }
  .front-label__variety {
    font-family: "Cormorant Garamond", serif; font-weight: 500;
    font-size: 3.6em; letter-spacing: 0.04em; line-height: 1.1;
  }
  .front-label__vintage { font-family: "Cormorant Garamond", serif; font-size: 2.8em; line-height: 1; }
  .front-label__origin { font-size: 1.1em; letter-spacing: 0.08em; color: var(--ink-grey); margin-top: 1.6em; }

  /* ---------- Back label ---------- */
  .back-label {
    position: absolute; left: 630px; top: 60px; width: 500px; height: 640px;
    background: var(--label-black); overflow: hidden;
    box-shadow: 0 6px 16px rgba(0,0,0,.25);
    font-size: 10px;
  }
  .back-label__art {
    position: absolute; left: 0; top: 0; width: 100%; height: 200px;
    background: linear-gradient(180deg, #2a2a2c 0%, #1a1a1b 70%, var(--label-black) 100%);
  }
  .back-label .brand-mark { top: 30px; }
  .back-label .brand-mark__circle { width: 64px; height: 64px; border-width: 4px; margin-bottom: 12px; }
  .back-label .brand-mark__name { font-size: 36px; }
  .back-label .brand-mark__sub { font-size: 18px; }

  .tasting-notes {
    position: absolute; left: 50px; top: 210px; width: 400px;
    text-align: center; font-size: 14px; line-height: 1.45; color: var(--ink-white);
  }
  .tasting-notes p + p { margin-top: 10px; }

  .legal {
    position: absolute; left: 40px; top: 460px; width: 420px; height: 120px;
    display: flex; align-items: center; gap: 14px;
  }
  .legal__drinks { display: flex; flex-direction: column; align-items: center; font-size: 11px; line-height: 1.2; }
  .legal__badges { display: flex; flex-direction: column; gap: 8px; }
  .badge-circle { width: 34px; height: 34px; border-radius: 50%; background: var(--ink-white); }
  .badge-plain { width: 90px; height: 34px; border-radius: 17px; background: var(--ink-white); }
  .legal__text { font-size: 9px; font-weight: 700; line-height: 1.3; text-transform: uppercase; }
  .legal__text strong { display: block; font-size: 14px; line-height: 1.15; }
  .legal__bottles {
    width: 70px; height: 80px;
    background: linear-gradient(180deg, #444 0%, #222 100%);
    border-radius: 4px;
  }
  .back-label__url {
    position: absolute; left: 0; bottom: 22px; width: 100%;
    text-align: center; font-size: 15px; letter-spacing: 0.04em;
  }
</style>
</head>
<body>

  <section class="front-label front-label--main">
    <div class="front-label__art" role="img" aria-label="Grey-scale illustration of a grape bunch and vine leaves growing as a tree over a line-drawn city skyline"></div>
    <div class="brand-mark">
      <div class="brand-mark__circle"></div>
      <span class="brand-mark__name">Harrowby</span>
      <span class="brand-mark__sub">Wine</span>
    </div>
    <div class="front-label__details">
      <p class="front-label__region">MARLBOROUGH</p>
      <p class="front-label__variety">RIESLING</p>
      <p class="front-label__vintage">2015</p>
      <p class="front-label__origin">WINE OF NEW ZEALAND</p>
    </div>
  </section>

  <section class="back-label">
    <div class="back-label__art" role="img" aria-label="Faint grey illustration of grapes and vine leaves"></div>
    <div class="brand-mark">
      <div class="brand-mark__circle"></div>
      <span class="brand-mark__name">Harrowby</span>
      <span class="brand-mark__sub">Wine</span>
    </div>
    <div class="tasting-notes">
      <p>Crisp, light amber colour with good acids. The nose is reminiscent of freshly cut herbs with a hint of mint.</p>
      <p>It will enhance rather than overpower any dish. A wonderful complement to any light dish and delightfully refreshing.</p>
      <p>Serve lightly chilled.</p>
    </div>
    <div class="legal">
      <div class="legal__drinks">
        <svg width="28" height="60" viewBox="0 0 28 60" aria-hidden="true">
          <path d="M10 2h8v12c6 3 8 8 8 14v30H2V28c0-6 2-11 8-14z" fill="#f2f2f2"/>
          <text x="14" y="42" font-size="10" font-family="Open Sans, sans-serif" font-weight="700" text-anchor="middle" fill="#0d0d0e">7.5</text>
        </svg>
        <span>13%</span>
        <span>750ml</span>
      </div>
      <div class="legal__badges">
        <div class="badge-circle"></div>
        <div class="badge-plain"></div>
      </div>
      <div class="legal__text">
        Produced and bottled by<br>Kereru Bay Wines Marlborough NZ
        <strong>Distributed by<br>Harrowby Imports Ltd.<br>Drink responsibly</strong>
      </div>
      <div class="legal__bottles" role="img" aria-label="Outline illustration of three wine bottles"></div>
    </div>
    <p class="back-label__url">www.harrowbyimports.co.nz</p>
  </section>

  <section class="front-label front-label--variant" style="left:50px">
    <div class="front-label__art" role="img" aria-label="Grey-scale illustration of a grape vine tree over a city skyline"></div>
    <div class="brand-mark"><div class="brand-mark__circle"></div><span class="brand-mark__name">Harrowby</span><span class="brand-mark__sub">Wine</span></div>
    <div class="front-label__details">
      <p class="front-label__region">MARLBOROUGH</p>
      <p class="front-label__variety">SAUVIGNON BLANC</p>
      <p class="front-label__vintage">2015</p>
      <p class="front-label__origin">WINE OF NEW ZEALAND</p>
    </div>
  </section>

  <section class="front-label front-label--variant" style="left:335px">
    <div class="front-label__art" role="img" aria-label="Grey-scale illustration of a grape vine tree over a city skyline"></div>
    <div class="brand-mark"><div class="brand-mark__circle"></div><span class="brand-mark__name">Harrowby</span><span class="brand-mark__sub">Wine</span></div>
    <div class="front-label__details">
      <p class="front-label__region">MARLBOROUGH</p>
      <p class="front-label__variety">PINOT NOIR</p>
      <p class="front-label__vintage">2015</p>
      <p class="front-label__origin">WINE OF NEW ZEALAND</p>
    </div>
  </section>

  <section class="front-label front-label--variant" style="left:620px">
    <div class="front-label__art" role="img" aria-label="Grey-scale illustration of a grape vine tree over a city skyline"></div>
    <div class="brand-mark"><div class="brand-mark__circle"></div><span class="brand-mark__name">Harrowby</span><span class="brand-mark__sub">Wine</span></div>
    <div class="front-label__details">
      <p class="front-label__region">MARLBOROUGH</p>
      <p class="front-label__variety">CHARDONNAY</p>
      <p class="front-label__vintage">2015</p>
      <p class="front-label__origin">WINE OF NEW ZEALAND</p>
    </div>
  </section>

  <section class="front-label front-label--variant" style="left:905px">
    <div class="front-label__art" role="img" aria-label="Grey-scale illustration of a grape vine tree over a city skyline"></div>
    <div class="brand-mark"><div class="brand-mark__circle"></div><span class="brand-mark__name">Harrowby</span><span class="brand-mark__sub">Wine</span></div>
    <div class="front-label__details">
      <p class="front-label__region">MARLBOROUGH</p>
      <p class="front-label__variety">PINOT GRIS</p>
      <p class="front-label__vintage">2015</p>
      <p class="front-label__origin">WINE OF NEW ZEALAND</p>
    </div>
  </section>

</body>
</html>
```